Website design for Cloud Scheduling Company

We have a design build that is based on a corporate template. the structure and content is there but the design does not match the 'feel' of what we are going for from a design perspective.
http://plumvexo.com/demo/fen/

please follow this structure for the site layout but add new ideas also.

Scheduling is boring and typically a serious topic, with our new logo we are looking to bring a quirky, fun feeling to what our site does.

It is a powerful scheduling platform that is used mainly in Volunteer environments and we want our brand to reflect this.

A lot of sites use images of real people in photographs but i would like to see us use more vector graphics and illustrations in the design so it is a bit more exciting.

The homepage should have a large screen capture of the app on different devices (large monitor, tablet, and smartphone) which is pretty standard for this type of website.i have attached a jpeg where you can get images from as well as the logo so you can get a sense of the look and feel.

this is what I envision being the image in the main banner as it showcases the application https://www.trindlesk.ca/search?q=responsive&biw=1920&bih=920&source=lnms&tbm=isch&sa=X&ved=0ahUKEwiAlqahjv_KAhXrlIMKHToqB5oQ_AUIBigB#imgrc=a75LOlLuwcKyqM%3A

Again, what I need for this project is a design for the site at http://plumvexo.com/demo/fen/. it is already coded but i need a netter design. focus on homepage, pricing page and a general subpage please.

Target Market(s)

Volunteer organization Administrators

Industry/Entity Type

It Company

Number of Pages Required

3 page

Font styles to use
Sans Serif

Colors
0355a3
f37122

Requirements
Nice to have
• use graphics instead of photographs. you can include some photos but i want the look and feel to be consistent with the playfulness of the logo so the site isnt too serious. The site still has to be professional.

```html
<!DOCTYPE html>
<html lang="en">
<head>
<meta charset="utf-8">
<title>fenscheduling — Cloud Scheduling</title>
<link href="https://fonts.googleapis.com/css2?family=Roboto:wght@300;400;500;700&family=Source+Sans+3:wght@300;400;600&display=swap" rel="stylesheet">
<style>
:root{
  --blue:#0355a3;
  --blue-band:#236199;
  --navy:#0d3a63;
  --navy-deep:#0a2b4b;
  --navy-bar:#08223c;
  --orange:#f37122;
  --orange-light:#f99a3a;
  --card:#e4ecf3;
  --paper:#f6f6f6;
  --ink:#555b61;
  --ink-soft:#8a9096;
  --white:#ffffff;
}
*{margin:0;padding:0;box-sizing:border-box}
html,body{width:1200px;height:2880px;overflow:hidden}
body{position:relative;background:var(--paper);font-family:"Roboto",sans-serif;color:var(--ink)}
a{text-decoration:none;color:inherit}
h1,h2,h3,h4{font-weight:400}
.abs{position:absolute}

/* hero */
.hero{left:0;top:0;width:1200px;height:426px;
  background:radial-gradient(ellipse 900px 500px at 620px 140px,#5a9bd4 0%,#3b80c0 40%,#2a6aab 75%,#1f5d9c 100%)}
.logo-pill{left:173px;top:23px;width:301px;height:73px;border-radius:37px;background:var(--white);
  display:flex;align-items:center;justify-content:center;gap:10px}
.logo-pill .mark{width:30px;height:30px;border-radius:50%;background:var(--blue)}
.logo-pill .name{font-weight:700;font-size:27px;color:var(--blue);letter-spacing:-0.3px}
.nav{top:46px;left:559px}
.nav a{position:absolute;top:0;color:var(--white);font-size:15px;font-weight:500;letter-spacing:2.4px;white-space:nowrap}
.nav a::after{content:"";position:absolute;left:0;right:3px;bottom:-10px;height:3px;background:var(--orange)}
.hero-title{left:173px;top:160px;width:345px;color:var(--white)}
.hero-title h1{font-size:31px;font-weight:700;letter-spacing:0;line-height:1;white-space:nowrap}
.hero-title h2{font-size:19.5px;font-weight:400;letter-spacing:0.2px;margin-top:8px;line-height:1;white-space:nowrap}
.hero-lead{left:173px;top:242px;width:320px;color:var(--white);font-size:16px;line-height:24px}
.btn{border-radius:999px;background:linear-gradient(var(--orange-light),var(--orange));color:var(--white);
  display:flex;align-items:center;justify-content:center;font-family:"Roboto",sans-serif;text-transform:uppercase}
.btn-learn{left:173px;top:386px;width:301px;height:79px;font-size:29px;font-weight:500;box-shadow:0 4px 8px rgba(0,0,0,.18)}
.device-shot{border-radius:6px}
.hero-devices{left:524px;top:198px;width:586px;height:297px;
  background:linear-gradient(160deg,#e9eef3 0%,#cfd8e1 55%,#9aa7b4 100%)}

/* benefits */
.mascot{background:linear-gradient(160deg,#2f78b9 0%,#1e5a96 70%,#1a4f85 100%);border-radius:40px 40px 30px 30px}
.mascot-hero{left:209px;top:638px;width:213px;height:292px}
.benefit-card{left:482px;top:580px;width:541px;height:365px;background:var(--card);border-radius:26px}
.benefit-card::before{content:"";position:absolute;left:-26px;top:174px;border:26px solid transparent;border-left:0;border-right-color:var(--card)}
.benefit{position:absolute;left:36px;display:flex;align-items:center}
.benefit .icon{width:88px;height:88px;border-radius:50%;background:var(--white);display:flex;align-items:center;justify-content:center;flex:none}
.benefit .copy{margin-left:35px}
.benefit h3{font-size:29px;font-weight:700;color:var(--blue);line-height:1;letter-spacing:-0.3px;white-space:nowrap}
.benefit p{font-size:15px;color:var(--ink-soft);line-height:19px;margin-top:5px;width:365px}

/* clients */
.band{left:0;width:1200px;background:var(--blue-band);color:var(--white);text-align:center}
.band-clients{top:1039px;height:94px;display:flex;align-items:center;justify-content:center;
  font-family:"Source Sans 3",sans-serif;font-size:36px;letter-spacing:2px}
.clients{left:0;top:1133px;width:1200px;height:182px;background:var(--white)}
.client-row{position:absolute;top:66px;left:150px;width:900px;display:flex;justify-content:space-between;align-items:center}
.client{display:flex;align-items:center;gap:8px;font-family:"Source Sans 3",sans-serif;font-size:18px;font-weight:600;color:#8e9398;letter-spacing:.5px}
.client .dot{width:12px;height:12px;border-radius:50%;background:#b4b8bc}
.view-all{position:absolute;left:0;width:1200px;top:132px;text-align:center;font-size:23px;font-weight:500;color:var(--blue)}
.view-all span{border-bottom:2px solid var(--blue)}

/* features */
.features-title{left:175px;top:1380px;font-family:"Source Sans 3",sans-serif;font-size:37px;color:var(--blue);letter-spacing:2px}
.features-copy{left:173px;top:1464px;width:430px;font-family:"Source Sans 3",sans-serif;font-size:22px;line-height:34px;color:var(--ink);letter-spacing:.3px}
.btn-why{left:167px;top:1686px;width:442px;height:71px;font-size:34px;font-weight:500;box-shadow:0 4px 8px rgba(0,0,0,.15)}
.feature-devices{left:624px;top:1428px;width:403px;height:310px;
  background:linear-gradient(160deg,#eef2f6 0%,#d3dbe3 55%,#2a3038 100%)}

/* demo band */
.band-demo{top:1834px;height:126px;display:flex;align-items:center;justify-content:center;
  font-family:"Source Sans 3",sans-serif;font-size:25px;letter-spacing:.6px}
.band-demo a{color:var(--white);border-bottom:2px solid var(--white);margin-left:8px}

/* contact */
.contact-title{left:0;width:1200px;top:2030px;text-align:center;font-family:"Source Sans 3",sans-serif;font-size:37px;font-weight:400;color:var(--blue);letter-spacing:2px}
.mascot-contact{left:205px;top:2137px;width:106px;height:154px}
.field{position:absolute;border-bottom:1px solid #e0e2e4;height:38px;padding-top:2px;font-family:"Source Sans 3",sans-serif;font-size:16px;color:#a4a9ae}
.btn-send{left:586px;top:2344px;width:209px;height:35px;font-size:11px;font-weight:700;letter-spacing:1px;gap:14px}
.form-note{left:0;width:1200px;top:2394px;text-align:center;font-size:11px;color:var(--ink-soft)}

/* footer */
.footer{left:0;top:2454px;width:1200px;height:359px;background:linear-gradient(var(--navy),var(--navy-deep));color:#c6d3df}
.footer-brand{position:absolute;left:173px;top:84px;display:flex;align-items:center;gap:10px;color:var(--white);font-weight:700;font-size:21px}
.footer-brand .mark{width:24px;height:24px;background:var(--white)}
.foot-address{position:absolute;font-size:13px;line-height:22px;text-align:center}
.foot-head{position:absolute;top:86px;font-size:13px;font-weight:500;letter-spacing:2.4px;color:var(--white)}
.foot-links{position:absolute;left:430px;top:130px;list-style:none;font-size:13px;line-height:22.5px;color:var(--white)}
.subscribe-input{position:absolute;left:563px;top:2598px;width:266px;height:38px;background:var(--white);
  display:flex;align-items:center;justify-content:center;font-size:13px;color:#a4a9ae}
.btn-subscribe{left:637px;top:2657px;width:119px;height:31px;font-size:10px;font-weight:700;letter-spacing:.6px}
.social{position:absolute;left:897px;top:206px;display:flex;gap:14px}
.social span{width:12px;height:12px;border-radius:50%;background:#c6d3df}
.copyright{left:0;top:2813px;width:1200px;height:67px;background:var(--navy-bar);display:flex;align-items:center;justify-content:center;font-size:11px;color:#8fa3b7}
</style>
</head>
<body>

<section class="abs hero" aria-label="Hero">
  <div class="abs logo-pill"><span class="mark"></span><span class="name">fenscheduling</span></div>
  <nav class="abs nav" aria-label="Main">
    <a href="#" style="left:0">HOME</a>
    <a href="#" style="left:111px">ABOUT</a>
    <a href="#" style="left:222px">SERVICES</a>
    <a href="#" style="left:363px">CONTACT</a>
  </nav>
  <div class="abs hero-title">
    <h1>FREE YOURSELF FROM</h1>
    <h2>MUNDANE REPETITIVE SCHEDULING</h2>
  </div>
  <p class="abs hero-lead">FEN Scheduling makes the Scheduling process simple for you and even simpler for your Volunteers</p>
</section>
<div class="abs device-shot hero-devices" role="img" aria-label="App screen capture on monitor, tablets, phone and laptop"></div>
<a class="abs btn btn-learn" href="#">Learn More</a>

<section aria-label="Benefits">
  <div class="abs mascot mascot-hero" role="img" aria-label="Owl mascot illustration with clock eye"></div>
  <div class="abs benefit-card">
    <div class="benefit" style="top:22px">
      <div class="icon">
        <svg width="34" height="46" viewBox="0 0 34 46" fill="none" stroke="#1d5c9a" stroke-width="2.5"><rect x="2" y="2" width="30" height="42" rx="4"/><rect x="7" y="8" width="20" height="26"/><circle cx="17" cy="39" r="1.5" fill="#1d5c9a"/></svg>
      </div>
      <div class="copy"><h3>Web &amp; Mobile ready</h3><p>Schedule at your desk or on the go</p></div>
    </div>
    <div class="benefit" style="top:131px">
      <div class="icon">
        <svg width="48" height="48" viewBox="0 0 48 48" fill="none" stroke="#1d5c9a" stroke-width="2.5" stroke-linejoin="round"><path d="M24 4v40M24 4l-6 7M24 4l6 7M24 26L8 12M8 12v8M8 12h8M24 26l16-14M40 12v8M40 12h-8"/></svg>
      </div>
      <div class="copy"><h3>Incredibly Flexible</h3><p>Manage 10 Volunteers or 1000. Our users have very unique needs and so do you, and we can help!</p></div>
    </div>
    <div class="benefit" style="top:237px">
      <div class="icon">
        <svg width="52" height="48" viewBox="0 0 52 48" fill="none" stroke="#1d5c9a" stroke-width="2.5"><circle cx="18" cy="28" r="11" stroke-dasharray="4 3"/><circle cx="18" cy="28" r="5"/><circle cx="38" cy="14" r="8" stroke-dasharray="3 3"/><circle cx="38" cy="14" r="3"/><circle cx="40" cy="38" r="6" stroke-dasharray="3 2"/></svg>
      </div>
      <div class="copy"><h3>Free Upgrades &amp; Support</h3><p>Maintenance fees aer a thing of the past. the system will always be kept curretnt with no additional fees.</p></div>
    </div>
  </div>
</section>

<section aria-label="Our clients">
  <h2 class="abs band band-clients">OUR CLIENTS</h2>
  <div class="abs clients">
    <div class="client-row">
      <span class="client"><span class="dot"></span>Halden</span>
      <span class="client"><span class="dot"></span>Brightfold</span>
      <span class="client"><span class="dot"></span>Crestline</span>
      <span class="client"><span class="dot"></span>Marlow Studio</span>
      <span class="client"><span class="dot"></span>Oakrow</span>
      <span class="client"><span class="dot"></span>Tidewell</span>
    </div>
    <div class="view-all"><span>View all</span></div>
  </div>
</section>

<section aria-label="Features">
  <h2 class="abs features-title">FEATURES</h2>
  <p class="abs features-copy">We create &amp; craft projects that ooze creativity in every aspect. We try to create a benchmark in everything we do.<br>Take a moment to browse through some of our recent completed work</p>
  <a class="abs btn btn-why" href="#">Find Out Why</a>
  <div class="abs device-shot feature-devices" role="img" aria-label="Dashboard charts shown on monitor, tablet and phone with owl mascot"></div>
</section>

<div class="abs band band-demo">Like Fen Scheduler? <a href="#">Download a Demo</a></div>

<section aria-label="Contact us">
  <h2 class="abs contact-title">CONTACT US</h2>
  <div class="abs mascot mascot-contact" role="img" aria-label="Small owl mascot illustration"></div>
  <div class="field" style="left:374px;top:2130px;width:308px">Name</div>
  <div class="field" style="left:708px;top:2130px;width:300px">Email Address</div>
  <div class="field" style="left:374px;top:2190px;width:212px">Phone</div>
  <div class="field" style="left:614px;top:2190px;width:394px">Subject</div>
  <div class="field" style="left:374px;top:2250px;width:634px">Subject</div>
  <a class="abs btn btn-send" href="#">
    <svg width="16" height="12" viewBox="0 0 16 12" fill="none" stroke="#fff" stroke-width="1.5"><rect x="1" y="1" width="14" height="10"/><path d="M1 1l7 6 7-6"/></svg>
    Send Message</a>
  <p class="abs form-note">We'll do our best to get back to you within 1-2 working hours.</p>
</section>

<footer class="abs footer">
  <div class="footer-brand"><span class="mark"></span>fenscheduling</div>
  <p class="foot-address" style="left:173px;top:140px;width:170px">123 Fen Ave, Suite 999<br>San Francisco, CA 999999</p>
  <p class="foot-address" style="left:173px;top:200px;width:170px">123 Fen Ave, Suite 999<br>San Francisco, CA 999999</p>
  <h4 class="foot-head" style="left:430px">SITE LINKS</h4>
  <ul class="foot-links"><li>Top</li><li>About</li><li>Works</li><li>Services</li><li>Contact</li></ul>
  <h4 class="foot-head" style="left:652px">SUBSCRIBE</h4>
  <h4 class="foot-head" style="left:906px">CONTACT</h4>
  <p class="foot-address" style="left:861px;top:140px;width:170px">123 Fen Ave, Suite 999<br>San Francisco, CA 999999</p>
  <div class="social"><span></span><span></span><span></span><span></span></div>
</footer>
<div class="subscribe-input">Your Email Address</div>
<a class="abs btn btn-subscribe" href="#">Subscribe Now</a>
<div class="abs copyright">Copyright fenscheduling 2015 | All Rights Reserved</div>

</body>
</html>
```